Revamp my web site design

Willowbrook Care Practitioners is a not for profit organisation focused on providing emotional support and counselling services to those with cancer or affected by cancer including those bereaved.

Our web site is intended to welcome suffers to engage with the services of its members and is also provided to encourage additional counsellors to join the organisation and then supports its members with access to materials and courses to extend their professional development.

We have a limited budget and seek to not only improve the attractiveness of the site but also improve the functionality and ease of maintenance. Especially site administrtaion should allow for uploading documents, adding new members, news and events easily.

Existing site is www.willowbrookcare.com.au

```html
<!DOCTYPE html>
<html lang="en">
<head>
<meta charset="utf-8">
<title>Willowbrook Care</title>
<link href="https://fonts.googleapis.com/css2?family=Source+Sans+3:wght@300;400;600&display=swap" rel="stylesheet">
<style>
:root{
  --green-dark:#1f6b12;
  --green:#3f9a14;
  --green-light:#a6e22a;
  --yellow:#ffd200;
  --yellow-deep:#f7b800;
  --orange:#f8a300;
  --heading-green:#1c5a12;
  --text:#555;
  --text-light:#7a7a7a;
  --panel-top:#4d7047;
  --panel-bottom:#1f3a1c;
  --footer-bg:#f4f4f4;
  --rule:#dedede;
}
*{margin:0;padding:0;box-sizing:border-box}
html,body{width:1061px;height:1200px;overflow:hidden;background:#fff}
body{position:relative;font-family:"Source Sans 3",sans-serif;color:var(--text)}
.header-bg{position:absolute;left:0;top:0;width:1061px;height:370px}
.brand{position:absolute;left:117px;top:44px;display:flex;align-items:center;gap:10px}
.brand-dot{width:34px;height:34px;border-radius:50%;background:var(--yellow)}
.brand-name{font-size:33px;font-weight:400;color:var(--yellow);letter-spacing:.5px}
.main-nav{position:absolute;left:111px;top:98px;width:840px;height:43px;display:flex;
  background:linear-gradient(#ffe233,var(--yellow-deep));border-radius:3px 3px 0 0}
.main-nav a{display:flex;align-items:center;justify-content:center;font-size:16.5px;color:#333;
  text-decoration:none;border-right:1px solid #d99e00}
.main-nav a:last-child{border-right:0}
.hero{position:absolute;left:111px;top:141px;width:840px;height:302px;
  background:linear-gradient(110deg,#d9dcdc 0%,#eef0f0 40%,#c9ced0 65%,#e9ecec 100%)}
.hero-caption{position:absolute;left:15px;top:166px;width:321px;height:93px;
  background:rgba(37,66,34,.92);border-radius:0 3px 3px 0;padding:20px 0 0 22px;color:#fff}
.hero-caption h1{font-weight:300;font-size:25px;line-height:1.1}
.hero-caption p{font-weight:300;font-size:16px;margin-top:6px}
.hero-dots{position:absolute;left:397px;top:344px;display:flex;gap:3px}
.hero-dots span{width:10px;height:10px;border-radius:50%;background:#fff}
.hero-dots{top:283px}
.feature{position:absolute;top:463px;width:254px}
.feature-img{width:254px;height:100px;border-radius:3px}
.feature h2{font-weight:400;font-size:19px;color:var(--heading-green);margin-top:12px;margin-left:3px}
.feature p{font-weight:300;font-size:12px;line-height:19px;color:var(--text-light);margin:6px 0 0 3px;width:256px}
.btn{display:inline-block;background:linear-gradient(#ffc21a,var(--orange));color:#fff;font-size:11.5px;
  width:96px;height:29px;line-height:29px;text-align:center;border-radius:3px;margin:10px 0 0 2px;
  box-shadow:0 1px 1px rgba(0,0,0,.2)}
.rule{position:absolute;left:111px;top:750px;width:840px;height:1px;background:var(--rule)}
.intro{position:absolute;left:114px;top:778px;width:556px}
.intro h2{font-weight:300;font-size:21px;color:#333}
.intro h3{font-weight:300;font-size:15px;color:#333;margin-top:2px}
.intro p{font-size:11.3px;line-height:20px;color:#555;margin-top:8px}
.side-panel{position:absolute;left:698px;width:253px;height:122px;border-radius:3px;
  background:linear-gradient(var(--panel-top),var(--panel-bottom));padding:13px 0 0 21px;color:#fff}
.side-panel h2{font-weight:400;font-size:20px}
.side-panel p{font-weight:300;font-size:11.5px;line-height:18px;margin-top:3px}
.side-btn{display:inline-block;margin-top:8px;background:#3d5a38;border:1px solid #5f7b5a;
  font-size:9.5px;padding:4px 10px;border-radius:2px}
.site-footer{position:absolute;left:0;top:1092px;width:1061px;height:108px;background:var(--footer-bg)}
.footer-nav{position:absolute;left:113px;top:27px;font-size:13px;color:#333}
.footer-nav span{margin:0 7px;color:#666}
.copyright{position:absolute;left:115px;top:55px;font-size:10px;font-weight:300;color:#666}
.social{position:absolute;left:883px;top:36px;display:flex;gap:4px}
.social i{width:20px;height:20px;border-radius:3px;background:#3b8ed8}
</style>
</head>
<body>
<svg class="header-bg" viewBox="0 0 1061 370" preserveAspectRatio="none" aria-hidden="true">
  <defs>
    <linearGradient id="hg" x1="0" y1="0" x2="1" y2="0">
      <stop offset="0" stop-color="#2f8a12"/>
      <stop offset=".55" stop-color="#3f9d12"/>
      <stop offset="1" stop-color="#a8e028"/>
    </linearGradient>
  </defs>
  <path d="M0 0H1061V363Q530 340 0 352Z" fill="url(#hg)"/>
  <rect width="1061" height="4" fill="#0f3d08"/>
  <path d="M0 300Q200 220 420 250" stroke="#9be03a" stroke-width="2" fill="none" opacity=".4"/>
  <path d="M820 120Q950 170 1061 150" stroke="#e8ff9a" stroke-width="2" fill="none" opacity=".5"/>
</svg>

<div class="brand"><span class="brand-dot"></span><span class="brand-name">Willowbrook Care</span></div>

<nav class="main-nav">
  <a style="width:97px">Home</a><a style="width:101px">About Us</a><a style="width:78px">News</a>
  <a style="width:82px">Events</a><a style="width:90px">Articles</a><a style="width:156px">Find a Counsellor</a>
  <a style="width:102px">Members</a><a style="width:134px">Contact Us</a>
</nav>

<section class="hero" role="img" aria-label="Photo of a nurse attending a patient during treatment">
  <div class="hero-caption">
    <h1>Medical Cancer Counselling</h1>
    <p>Duis sed tellus et tortor vestibulum</p>
  </div>
  <div class="hero-dots"><span></span><span></span><span></span><span></span></div>
</section>

<article class="feature" style="left:121px">
  <div class="feature-img" role="img" aria-label="Photo of two women talking" style="background:linear-gradient(90deg,#cdb894,#e5d7bc,#9c8a6c)"></div>
  <h2>What is Counselling?</h2>
  <p>Counselling is a private and confidential meeting to explore difficulties you are having. Your coun-sellor will be supportive but will not give advice, or tell you what to do.</p>
  <span class="btn">READ MORE</span>
</article>
<article class="feature" style="left:403px">
  <div class="feature-img" role="img" aria-label="Photo of a nurse caring for a patient" style="background:linear-gradient(90deg,#d8dbe0,#e8a9b9,#eaeaea)"></div>
  <h2>Why Cancer Counselling?</h2>
  <p>Research shows that counselling can play a sig-nificant part in helping individuals and families face and meet the many challenges implicit in a cancer diagnosis</p>
  <span class="btn">READ MORE</span>
</article>
<article class="feature" style="left:686px">
  <div class="feature-img" role="img" aria-label="Photo of a doctor speaking with a young man" style="background:linear-gradient(90deg,#eceae6,#f4f4f2,#9a4a44)"></div>
  <h2>How will it help me?</h2>
  <p>In our experience, many people faced with a cancer diagnosis find it very helpful to be able to talk about how they are really feeling to someone who is not trying to make them feel better</p>
  <span class="btn">READ MORE</span>
</article>

<div class="rule"></div>

<section class="intro">
  <h2>Willowbrook Care Practitioners</h2>
  <h3>A diagnosis of cancer is a devastating experience for most people.</h3>
  <p>Many people can get support by talking to close family or friends. However, it can sometimes help to talk to someone from outside of that circle who has been trained to listen and help you explore your feelings. You may feel as if you are riding an emotional rollercoaster. Often talking of your distress to those close to you can be difficult and painful.</p>
  <p>When someone is diagnosed with cancer, they and their family can feel shocked, numb, directionless and afraid. They often feel they need to talk things through in confidence with someone who understands the emotional challenges of cancer.</p>
  <p>Talking to a counsellor or psychologist experienced in cancer issues can ease the sense of isolation you may feel and help you find ways to face the challenges ahead.</p>
</section>

<aside class="side-panel" style="top:781px">
  <h2>Find A Counsellor</h2>
  <p>Duis tincidunt lectus quis dui viverra vestib<br>ulum Suspendisse vulputate aliquam</p>
  <span class="side-btn">CLICK HERE</span>
</aside>
<aside class="side-panel" style="top:914px">
  <h2>New &amp; Events</h2>
  <p>Duis tincidunt lectus quis dui viverra vestib<br>ulum Suspendisse vulputate aliquam</p>
  <span class="side-btn">CLICK HERE</span>
</aside>

<footer class="site-footer">
  <div class="footer-nav">Home<span>|</span>About Us<span>|</span>News<span>|</span>Events<span>|</span>Articles<span>|</span>Find a Counsellor<span>|</span>Members<span>|</span>Contact Us</div>
  <div class="copyright">Copyright © 2013 Company Name.&nbsp; All right reserved.&nbsp; Term of Use</div>
  <div class="social"><i></i><i style="background:#1f6fb2"></i><i style="background:#3b5ba8"></i></div>
</footer>
</body>
</html>
```